Business Card Design Project

I am a property development company requiring a professional looking business card.
The name of the my company is PLW CANOPIES. I have attached a couple of designs that I have created on my own, that can give you an idea of what I am after.
Above the wording PLW CANOPIES, I have a orange arc above these words to signify the sun is begining to rise above the horizon.
I have a few designs; Middle Rays, Side Rays, Horizontals Rays which are OK, but I am looking for the better design.
The Rear design of the card is what I had came up with. If you have a better design, I am happy to see it.
The design of the card can follow what I have came up with, or it can be totally different. The fonts needs to be adjusted to another font that is more suitable.
The colours that I have used is what I think I would like to stick with. As I have mentioned, the orange arc is to signify the sun rising. If you have a better colour scheme, I would consider it.
Looking at dealing with first home buyers and proffesional people.
Business

```html
<!DOCTYPE html>
<html lang="en">
<head>
<meta charset="utf-8">
<title>PLW Canopies – Business Card</title>
<link rel="stylesheet" href="https://fonts.googleapis.com/css2?family=Roboto+Condensed:wght@700&family=Roboto:wght@300&display=swap">
<style>
  :root {
    --card-bg: #fde1b4;
    --ink: #2b2826;
    --accent-orange: #f25c12;
    --sun-core: #f8a81c;
  }
  html, body {
    margin: 0;
    padding: 0;
    width: 1200px;
    height: 775px;
    overflow: hidden;
    background: var(--card-bg);
  }
  .business-card {
    position: relative;
    width: 1200px;
    height: 775px;
    background: var(--card-bg);
    font-family: "Roboto", "Helvetica Neue", Arial, sans-serif;
    color: var(--ink);
  }
  .brand-mark {
    position: absolute;
    left: 531px;
    top: 62px;
    width: 150px;
    height: 150px;
  }
  .brand-name {
    position: absolute;
    left: 0;
    right: 0;
    top: 236px;
    margin: 0;
    text-align: center;
    font-family: "Roboto Condensed", "Arial Narrow", sans-serif;
    font-weight: 700;
    font-size: 91px;
    line-height: 1;
    letter-spacing: 1px;
    color: var(--ink);
  }
  .brand-tagline {
    position: absolute;
    left: 0;
    right: 0;
    top: 342px;
    margin: 0;
    text-align: center;
    font-weight: 300;
    font-size: 38px;
    line-height: 1.1;
    color: var(--accent-orange);
  }
  .contact-details {
    position: absolute;
    left: 38px;
    top: 545px;
    margin: 0;
    padding: 0;
    list-style: none;
    font-weight: 300;
    font-size: 30px;
    line-height: 40.6px;
    color: var(--ink);
  }
</style>
</head>
<body>
  <main class="business-card">
    <svg class="brand-mark" viewBox="0 0 150 150" aria-hidden="true">
      <circle cx="75" cy="75" r="72" fill="var(--sun-core)"/>
    </svg>
    <h1 class="brand-name">PLW CANOPIES</h1>
    <p class="brand-tagline">Property Developments</p>
    <ul class="contact-details">
      <li class="contact-name">Marcus Lowe - Director</li>
      <li class="contact-address">48 Ferris Street, Kareela, NSW 2232, Australia</li>
      <li class="contact-phone">Tel: 0412 558 903</li>
      <li class="contact-email">Email: marcus@plwcanopies.com.au</li>
      <li class="contact-web">Web: www.plwcanopies.com.au</li>
    </ul>
  </main>
</body>
</html>
```